Wordpress Lifestyle Blog

Just to be clear - I have the domain and the wordpress site (which is messy). I need someone to help me complete a simple blog design and then go into the existing wordpress site, and get rid of all the existing rubbish and set up the templates please. If we progress with design can we please be clear about additional costs upfront which, of course, I appreciate is the case.

Need a lifestyle blog. It is called brightyearsahead.com. Aimed at the older woman but needs to look fresh and young, not old fashioned. Navigation will be Home, Fashion, Feelings, Fitness, Contact. I have a logo but not sure it will work at the moment so happy with stylised words.Will have social media links.

Need homepage (not overly long) to have a main slider for pics/videos. Then the three category boxes underneath linking through to 2nd level pages containing blogs for that category and then the actual blog page. Happy to be led by expertise if this is not gonna work.

Am really looking for something clean and fresh like a Marwyn type approach to be honest.

If you need any further direction please just ask - once design chosen I am looking to move quickly.

Thank you so much for looking at this brief

Target Market(s)

Women, 40 - 60 age group but with a younger outlook

Number of Pages Required

3 page

Colors

Designer to choose colors to be used in the design.

Requirements
Must have
• Reflect youth, fun, bright
• Lift easily into a wordpress format
Should not have
• Old, staid, frumpy,dark

```html
<!DOCTYPE html>
<html lang="en">
<head>
<meta charset="utf-8">
<title>Contact – Bright Years Ahead</title>
<link href="https://fonts.googleapis.com/css2?family=Quattrocento:wght@400;700&display=swap" rel="stylesheet">
<style>
  :root {
    --ink: #1f1f1f;
    --muted: #555555;
    --accent: #f0b7bd;
    --accent-strong: #eea3ab;
    --rule: #e6e6e6;
    --paper: #ffffff;
    --overlay: rgba(20, 20, 20, 0.72);
  }
  * { box-sizing: border-box; margin: 0; padding: 0; }
  html, body {
    width: 1168px; height: 1200px; overflow: hidden;
    background: var(--paper); color: var(--ink);
    font-family: "Quattrocento", Georgia, serif;
  }
  .page { position: relative; width: 1168px; height: 1200px; }

  .site-title {
    position: absolute; top: 44px; left: 0; width: 100%;
    text-align: center; font-size: 42px; font-weight: 400;
    letter-spacing: 1px; color: #8fb8e0;
  }
  .header-rule {
    position: absolute; top: 167px; left: 164px; width: 842px;
    border-top: 1px solid var(--rule);
  }
  .main-nav {
    position: absolute; top: 181px; left: 0; width: 100%;
    display: flex; justify-content: center; align-items: center; gap: 18px;
    font-size: 12px; letter-spacing: 0.2px;
  }
  .main-nav a { color: var(--ink); text-decoration: none; }
  .main-nav a.is-current { color: var(--accent-strong); }
  .main-nav svg { margin-left: 2px; }

  .page-title {
    position: absolute; top: 238px; left: 0; width: 100%;
    text-align: center; font-size: 54px; font-weight: 400; letter-spacing: -0.5px;
  }
  .title-rule {
    position: absolute; top: 321px; left: 532px; width: 100px;
    border-top: 2px solid var(--accent);
  }
  .page-lead {
    position: absolute; top: 340px; left: 0; width: 100%;
    text-align: center; font-size: 22px;
  }

  .contact-form label {
    position: absolute; font-size: 12.5px; color: var(--ink);
  }
  .contact-form .field {
    position: absolute; border: 1px solid #333; background: var(--paper);
  }
  .send-button {
    position: absolute; left: 165px; top: 603px; width: 69px; height: 37px;
    background: var(--accent); color: #fff; border: none;
    font-family: "Quattrocento", Georgia, serif; font-size: 11px; letter-spacing: 0.3px;
  }

  .social-links {
    position: absolute; top: 696px; left: 0; width: 100%;
    display: flex; justify-content: center; gap: 13px;
    font-size: 7.5px; color: var(--muted); letter-spacing: 0.2px;
  }
  .social-links span::before {
    content: ""; display: inline-block; width: 5px; height: 5px;
    border-radius: 50%; background: var(--muted); margin-right: 3px; vertical-align: middle;
  }

  .feed-title {
    position: absolute; top: 729px; left: 0; width: 100%;
    text-align: center; font-size: 18px;
  }
  .feed-grid {
    position: absolute; top: 756px; left: 0; width: 1168px; height: 389px;
    display: grid; grid-template-columns: repeat(6, 1fr); grid-template-rows: repeat(2, 1fr);
  }
  .feed-tile { position: relative; }
  .feed-tile.t1 { background: linear-gradient(160deg, #d9d4cf, #4a403a 60%, #bcb3ac); }
  .feed-tile.t2 { background: linear-gradient(170deg, #2f3b2d, #e8b948 45%, #8c8a8c); }
  .feed-tile.t3 { background: linear-gradient(160deg, #e9e4de, #e6b5a7 55%, #cfc7bf); }
  .feed-tile.t4 { background: linear-gradient(170deg, #6b5a4c, #ebe5dc 45%, #b8aca0); }
  .feed-tile.t5 { background: linear-gradient(170deg, #9aa48c, #dcd9cf 50%, #c4bfb4); }
  .feed-tile.t6 { background: linear-gradient(160deg, #2b2625, #3a2f2e 50%, #161414); }
  .feed-tile.t7 { background: linear-gradient(160deg, #c98a4a, #e6c070 45%, #2f3636); }
  .feed-tile.t8 { background: linear-gradient(160deg, #6e5b4c, #c9c6bd 50%, #8e9a8c); }
  .feed-tile.t9 { background: linear-gradient(170deg, #dcdad5, #6f7560 55%, #b0aca4); }
  .feed-tile.t10 { background: linear-gradient(170deg, #3d4a55, #e3e1dc 55%, #8a8f93); }
  .feed-tile.t11 { background: linear-gradient(170deg, #e4ddd2, #2a2624 55%, #cfc4b3); }
  .feed-tile.t12 { background: linear-gradient(170deg, #3b3b3e, #e6a6a0 55%, #8a8d90); }
  .feed-tile .tile-overlay {
    position: absolute; inset: 0; background: var(--overlay); color: #fff;
    display: flex; flex-direction: column; align-items: center; justify-content: center; gap: 9px;
    font-size: 9px;
  }
  .tile-stats { display: flex; gap: 10px; align-items: center; }
  .tile-stats span { display: inline-flex; align-items: center; gap: 3px; }

  .site-footer {
    position: absolute; top: 1173px; left: 0; width: 100%;
    font-size: 7.5px; color: var(--muted);
  }
  .site-footer .copyright { position: absolute; left: 281px; }
  .site-footer .back-to-top { position: absolute; left: 846px; top: 2px; font-size: 6.5px; }
</style>
</head>
<body>
<div class="page">
  <header>
    <div class="site-title">brightyearsahead</div>
    <div class="header-rule"></div>
    <nav class="main-nav">
      <a href="#">HOME</a>
      <a href="#">CATEGORIES</a>
      <a href="#">PAGES</a>
      <a href="#">ABOUT ME</a>
      <a href="#">GALLERY</a>
      <a href="#" class="is-current">CONTACT</a>
      <a href="#">SUBSCRIBE</a>
      <svg width="13" height="13" viewBox="0 0 13 13" aria-label="Search">
        <circle cx="5.3" cy="5.3" r="4" fill="none" stroke="#1f1f1f" stroke-width="2"/>
        <line x1="8.3" y1="8.3" x2="12" y2="12" stroke="#1f1f1f" stroke-width="2.2" stroke-linecap="round"/>
      </svg>
    </nav>
  </header>

  <main>
    <h1 class="page-title">GET IN TOUCH</h1>
    <div class="title-rule"></div>
    <p class="page-lead">I would love to hear from you</p>

    <form class="contact-form">
      <label style="left:165px; top:404px;">Your Name (required)</label>
      <div class="field" style="left:165px; top:422px; width:406px; height:36px;"></div>
      <label style="left:594px; top:404px;">Your Email (required)</label>
      <div class="field" style="left:594px; top:422px; width:406px; height:36px;"></div>
      <label style="left:165px; top:469px;">Your Message</label>
      <div class="field" style="left:165px; top:487px; width:835px; height:108px;"></div>
      <button type="button" class="send-button">SEND</button>
    </form>
  </main>

  <div class="social-links">
    <span>LIKE ON FACEPAGE</span>
    <span>FOLLOW ON CHIRPER</span>
    <span>FOLLOW ON SNAPGRAM</span>
    <span>GOSSIP ON BLOGHEART</span>
  </div>

  <h2 class="feed-title" style="font-weight:400;">Snapgram</h2>
  <section class="feed-grid">
    <div class="feed-tile t1" role="img" aria-label="Photo of a woman in a black strapless playsuit"></div>
    <div class="feed-tile t2" role="img" aria-label="Photo of a yellow ruffle crop top with gingham trousers"></div>
    <div class="feed-tile t3" role="img" aria-label="Photo of a woman in a pink gingham outfit and hat"></div>
    <div class="feed-tile t4" role="img" aria-label="Photo of a white off-shoulder lace set"></div>
    <div class="feed-tile t5" role="img" aria-label="Photo of a yellow top and white skirt on a terrace"></div>
    <div class="feed-tile t6" role="img" aria-label="Photo of a black lace top and cardigan"></div>
    <div class="feed-tile t7" role="img" aria-label="Photo of a yellow floral two-piece"></div>
    <div class="feed-tile t8" role="img" aria-label="Photo of green gingham shorts"></div>
    <div class="feed-tile t9" role="img" aria-label="Photo of a khaki wrap dress with a cane bag"></div>
    <div class="feed-tile t10" role="img" aria-label="Photo of a white corset top">
      <div class="tile-overlay">
        <div class="tile-stats">
          <span><svg width="9" height="8" viewBox="0 0 9 8"><path d="M4.5 7.3 1 3.9A2 2 0 0 1 4.5 1.4 2 2 0 0 1 8 3.9Z" fill="none" stroke="#fff" stroke-width="0.9"/></svg>6834</span>
          <span><svg width="9" height="8" viewBox="0 0 9 8"><path d="M4.5 0.8C2.3 0.8 0.8 2 0.8 3.6c0 .9.5 1.6 1.2 2.1L1.6 7.3 3.4 6.3c.4.1.7.1 1.1.1 2.2 0 3.7-1.2 3.7-2.8S6.7.8 4.5.8Z" fill="none" stroke="#fff" stroke-width="0.9"/></svg>28</span>
        </div>
        <div>Marla Corset Top ...</div>
      </div>
    </div>
    <div class="feed-tile t11" role="img" aria-label="Photo of a black slip dress with a straw bag"></div>
    <div class="feed-tile t12" role="img" aria-label="Photo of a pink gingham off-shoulder dress"></div>
  </section>

  <footer class="site-footer">
    <span class="copyright">Copyrights ©</span>
    <span class="back-to-top">BACK TO TOP</span>
  </footer>
</div>
</body>
</html>
```